Corbel Insurance Agency, Inc.
www.corbelinsagy.example
Project: Corbel Insurance Agency, Inc.
Corbel Insurance Agency, Inc. -
Creative Brief
Independent insurance agency created in 1938.
Like: Simple design and easy to use.
Service Oriented
Arial, Verdana, Times New Roman
left side
http://www.tallisinsagency.example/
http://pruett-insurance.example/

```html
<!DOCTYPE html>
<html lang="en">
<head>
<meta charset="utf-8">
<title>Corbel Insurance Agency, Inc.</title>
<link rel="stylesheet" href="https://fonts.googleapis.com/css2?family=Arimo:wght@400;700&display=swap">
<style>
:root{
  --page-top:#f4f4f2;
  --page-bottom:#dcdcd8;
  --ink:#1c1c1c;
  --muted:#8a8a8a;
  --teal:#22b3bd;
  --sky:#1f9ad6;
  --navy:#1443b0;
  --orange:#f08a0c;
  --orange-light:#f7a53a;
  --button-top:#f5f5f5;
  --button-bottom:#b9b9b9;
  --panel-top:#e6eef0;
  --panel-bottom:#c9d6da;
}
*{box-sizing:border-box;margin:0;padding:0}
html,body{width:1200px;height:971px;overflow:hidden}
body{
  position:relative;
  font-family:"Arimo",Arial,sans-serif;
  color:var(--ink);
  background:linear-gradient(180deg,var(--page-top),var(--page-bottom));
}
.abs{position:absolute}

/* top bar */
.sign-button{left:335px;top:20px;width:155px;height:28px;border-radius:14px;
  background:linear-gradient(var(--button-top),var(--button-bottom));border:1px solid #aaa;
  font-size:19px;text-align:center;line-height:26px}
.search-field{left:510px;top:20px;width:275px;height:28px;border-radius:14px;
  background:linear-gradient(#fff,#e2e2e2);border:1px solid #bbb}
.search-field svg{position:absolute;left:10px;top:6px}
.top-nav{right:22px;top:4px;font-size:17px;color:var(--muted);display:flex;gap:12px}
.top-nav span.sep{color:#bbb}

/* brand */
.brand-dot{left:52px;top:92px;width:66px;height:66px;border-radius:50%;background:#2b2b2b}
.brand{left:52px;top:168px;width:240px}
.brand-name{font-size:66px;font-weight:700;color:#2b2b2b;line-height:66px;letter-spacing:-1px}
.brand-sub{font-size:19px;font-weight:700;color:#2b2b2b;line-height:22px;margin-top:2px;white-space:nowrap}
.tagline{left:52px;top:262px;width:238px;height:18px;background:#111;color:#fff;
  font-size:12px;line-height:18px;padding-left:4px;white-space:nowrap}

/* hero */
.hero{left:327px;top:86px;width:863px;height:222px;
  background:linear-gradient(180deg,#3a7fc0 0%,#7fb4e0 55%,#c9dff2 100%)}
.hero-flag{left:719px;top:222px;width:471px;height:86px;background:var(--orange);
  color:#fff;font-size:32px;line-height:38px;padding:6px 0 0 36px}

/* tiles */
.tile{top:324px;width:212px;height:186px;padding:10px 10px 0}
.tile .photo{height:137px;background:linear-gradient(#b8a89a,#7e7064)}
.tile .caption{font-size:18px;text-align:center;line-height:30px;color:#fff}
.tile-business{left:332px;background:#d6e2ea}
.tile-business .caption{color:#1f55a8}
.tile-home{left:549px;background:var(--teal)}
.tile-home .photo{background:linear-gradient(#9ac6e6,#c58a55)}
.tile-car{left:763px;background:var(--sky)}
.tile-car .photo{background:linear-gradient(#9cc3e3,#5b6d7f)}
.tile-life{left:978px;width:212px;background:var(--navy)}
.tile-life .photo{background:linear-gradient(#d8c9b5,#a08772)}

/* side menu */
.side-menu{left:52px;top:332px;width:223px;list-style:none}
.side-menu li{height:48px;margin-bottom:9.5px;border-radius:10px;border:1px solid #999;
  background:linear-gradient(var(--button-top),var(--button-bottom));
  font-size:21px;text-align:center;line-height:46px;color:#222}
.side-menu li.current{background:linear-gradient(#7fdde3,var(--teal));color:#fff}

/* welcome */
.welcome{left:340px;top:530px;width:850px}
.welcome h1{font-size:31px;font-weight:400;line-height:36px;margin-bottom:2px}
.welcome p{font-size:18.5px;line-height:22px;text-align:justify}
.more-button{display:inline-block;border-radius:12px;background:linear-gradient(var(--orange-light),var(--orange));
  border:1px solid #c66c00;font-size:11px;color:#222;text-align:center;line-height:18px;height:20px}
.welcome .more-button{width:104px;margin-left:14px;vertical-align:middle;float:right;margin-top:1px}

/* offer panel */
.offer{left:335px;top:685px;width:402px;height:232px;padding:6px 18px;overflow:hidden;
  background:linear-gradient(var(--panel-top),var(--panel-bottom))}
.offer h2,.testimonials h2{font-size:27px;font-weight:400;line-height:32px;margin-bottom:4px}
.offer p{font-size:17px;line-height:19px;text-align:justify;width:366px}
.offer .more-button{position:absolute;left:266px;top:204px;width:118px}

/* testimonials */
.testimonials{left:758px;top:682px;width:432px}
.quote{display:flex;gap:10px;margin-bottom:10px;height:60px}
.quote .face{flex:0 0 64px;height:58px;border-radius:8px;background:linear-gradient(#c9b6a4,#8b7866)}
.quote p{font-size:10.5px;line-height:13px}

/* footer */
.social{top:913px;width:34px;height:34px;border-radius:6px}
.social-a{left:68px;background:#3b5b9a}
.social-b{left:108px;background:#35a9dd}
.copyright{right:28px;top:945px;font-size:11px;color:var(--muted)}
</style>
</head>
<body>

<div class="abs sign-button">Sign</div>
<div class="abs search-field">
  <svg width="16" height="16" viewBox="0 0 16 16"><circle cx="6.5" cy="6.5" r="4.5" fill="none" stroke="#555" stroke-width="1.6"/><line x1="10" y1="10" x2="14" y2="14" stroke="#555" stroke-width="1.8"/></svg>
</div>
<nav class="abs top-nav"><span>Home</span><span class="sep">|</span><span>Clients</span><span class="sep">|</span><span>Claims</span><span class="sep">|</span><span>Contact</span></nav>

<div class="abs brand-dot"></div>
<div class="abs brand">
  <div class="brand-name">Corbel</div>
  <div class="brand-sub">Insurance Agency, Inc.</div>
</div>
<div class="abs tagline">Protection for all your insurance needs</div>

<div class="abs hero" role="img" aria-label="Photo of a hawk in flight against a blue sky"></div>
<div class="abs hero-flag">Protection for all your<br>insurance needs</div>

<div class="abs tile tile-business"><div class="photo" role="img" aria-label="Photo of a business team at a meeting"></div><div class="caption">Protect your business</div></div>
<div class="abs tile tile-home"><div class="photo" role="img" aria-label="Photo of a family in front of their house"></div><div class="caption">Protect your home</div></div>
<div class="abs tile tile-car"><div class="photo" role="img" aria-label="Photo of a car on the road"></div><div class="caption">Protect your car</div></div>
<div class="abs tile tile-life"><div class="photo" role="img" aria-label="Photo of a parent with a child"></div><div class="caption">Protect your life</div></div>

<ul class="abs side-menu">
  <li class="current">Home</li>
  <li>About us</li>
  <li>Insurance plans</li>
  <li>Solutions</li>
  <li>Servises</li>
  <li>Support</li>
  <li>Contact</li>
</ul>

<section class="abs welcome">
  <h1>Welcome to Corbel Insuarance Agency</h1>
  <p>In law and economics, insurance is a form of risk management primarily used to hedge against the risk of a contingent, uncertain loss. Insurance is defined as the equitable transfer of the risk of a loss, from one entity to another, in exchange for payment. An insurer is a company selling the insurance; an insured, or policyholder, is the person or entity buying the insurance policy.<span class="more-button">More information</span></p>
</section>

<section class="abs offer">
  <h2>What we offer</h2>
  <p>In law and economics, insurance is a form of risk management primarily used to hedge against the risk of a contingent, uncertain loss. Insurance is defined as the equitable transfer of the risk of a loss, from one entity to another, in exchange for payment. An insurer is a company selling the</p>
  <div class="more-button">More information</div>
</section>

<section class="abs testimonials">
  <h2>Clients Testimonials</h2>
  <div class="quote"><div class="face" role="img" aria-label="Client portrait"></div><p>"In law and economics, insurance is a form of risk management primarily used to hedge against the risk of a contingent, uncertain loss. Insurance is defined as the equitable transfer of the risk of a loss, from one entity"</p></div>
  <div class="quote"><div class="face" role="img" aria-label="Client portrait"></div><p>"An insurer is a company selling the insurance; an insured, or policyholder, is the person or entity buying the insurance policy."</p></div>
  <div class="quote"><div class="face" role="img" aria-label="Client portrait"></div><p>"The insurance rate is a factor used to determine the amount to be charged for a certain amount of insurance coverage, called the premium. Risk management, the"</p></div>
</section>

<div class="abs social social-a" role="img" aria-label="Social network link"></div>
<div class="abs social social-b" role="img" aria-label="Social network link"></div>
<div class="abs copyright">© 2011 Corbel Insurance Agency, Inc. All rights reserved</div>

</body>
</html>
```